Luxury Wine Label for New Startup Winery

We need a wine label for our new winery startup. We have worked with a local designer but do not feel the resulting label / logo have the elevation required to present our brand as a luxury wine. Our winery is called "Harrowgate Vineyards" and we are focused on extremely high quality hand crafted artisan and estate wines from the Pacific Northwest.
We would like to see designs that utilize a tree line, or other imagery that represents the "Harrowgate" part of our company name. Another interesting feature could be wood grain.
A logo will be required based on your design so please design with this in mind:
This logo should be consistent with the wine bottle label design, and should be representative of our high end exclusive wine while giving a sense of place (Oregon/ Pacific Northwest.)
I will supply an image of the design we received from our local designer, PLEASE NOTE: in general we do like wood grain and tree line concepts but feel the execution was poorly done.
ATTN: Logo design should be suitable for use on: Bottles (Red wine/rose/white wine), Bussiness cards, vehicle signage, business signage, etc
P.S.:
If you have a design that is not outside the box we are still interested in seeing it.
Label is for a burgundy style bottle with a label height of 3.5 - 4" and a width of 3.5-4"
any label <= 4"x4" and >=3.5"x3.5" will be acceptable:
HOWEVER Width should be greater than or equal to height due to the bottle format
Target Market(s)
Wine enthusiasts with adequate discretionary budgets to afford $100 bottles of wine.
Industry/Entity Type
Wine / Winery
Requirements
Must have
- A sense of luxury, a feel of exclusivity, and a theme consistent with our product and brand name
Nice to have
- Tree line, wood grain or other wood themes. Serif fonts
Should not have
- anything cheesy, off topic, hard to read script fonts or anything that makes the label hard to read from a few feet away or too busy

```html
<!DOCTYPE html>
<html lang="en">
<head>
<meta charset="UTF-8">
<title>Harrowgate Vineyards — Syrah Label</title>
<link href="https://fonts.googleapis.com/css2?family=Cinzel:wght@500;600;700&display=swap" rel="stylesheet">
<style>
  :root {
    --canvas: #f4f4f4;
    --label-black: #141414;
    --stripe: #5a5a5a;
    --gold: #d9b27a;
    --gold-light: #ecd0a0;
    --gold-deep: #a9814c;
    --wood-dark: #2e211a;
    --wood-mid: #4a372b;
  }
  * { margin: 0; padding: 0; box-sizing: border-box; }
  html, body {
    width: 1200px; height: 1200px; overflow: hidden;
    background: var(--canvas);
  }
  .label {
    position: absolute;
    left: 250px; top: 95px;
    width: 700px; height: 1010px;
    background: var(--label-black);
    font-family: 'Cinzel', serif;
    color: var(--gold);
  }
  .stripes {
    position: absolute; left: 0; right: 0; height: 22px;
    background: repeating-linear-gradient(to bottom,
      var(--stripe) 0 1px, transparent 1px 5px);
    opacity: .7;
  }
  .stripes--top { top: 0; }
  .stripes--bottom { top: 790px; height: 36px; }

  .brand {
    position: absolute; left: 0; right: 0; top: 150px;
    display: flex; flex-direction: column; align-items: center; gap: 18px;
  }
  .brand__mark {
    width: 22px; height: 22px; border-radius: 50%;
    background: var(--gold);
  }
  .brand__name {
    font-weight: 600; font-size: 34px; letter-spacing: 3px;
    text-align: center; line-height: 1.25;
  }

  .region {
    position: absolute; left: 95px; right: 95px; top: 425px;
    padding: 14px 0;
    border-top: 1px solid var(--gold-deep);
    border-bottom: 1px solid var(--gold-deep);
    text-align: center;
    font-weight: 600; font-size: 32px; letter-spacing: 2px;
  }

  .treeline {
    position: absolute; left: 0; right: 0; top: 500px; height: 260px;
    background: linear-gradient(to bottom,
      transparent 0%, rgba(217,178,122,.35) 30%,
      var(--gold) 60%, var(--gold-deep) 80%, var(--label-black) 100%);
  }

  .variety {
    position: absolute; left: 0; right: 0; top: 850px; height: 112px;
    background: linear-gradient(to bottom, var(--wood-mid), var(--wood-dark));
    border-top: 2px solid var(--gold-deep);
    display: flex; align-items: center; justify-content: center;
  }
  .variety__name {
    font-weight: 700; font-size: 64px; letter-spacing: 4px;
    color: var(--gold-light);
  }

  .vintage {
    position: absolute; left: 0; right: 0; top: 968px;
    display: flex; align-items: center; gap: 14px;
  }
  .vintage__rule { flex: 1; height: 1px; background: var(--gold-deep); }
  .vintage__text {
    font-weight: 700; font-size: 26px; letter-spacing: 3px;
    color: var(--gold-light);
  }
</style>
</head>
<body>
  <main class="label">
    <div class="stripes stripes--top"></div>

    <div class="brand">
      <span class="brand__mark"></span>
      <p class="brand__name">Harrowgate<br>Vineyards</p>
    </div>

    <p class="region">Willamette Valley</p>

    <div class="treeline" role="img" aria-label="Gold foil silhouette of a conifer tree line along a rolling hill"></div>

    <div class="stripes stripes--bottom"></div>

    <div class="variety">
      <h1 class="variety__name">SYRAH</h1>
    </div>

    <div class="vintage">
      <span class="vintage__rule"></span>
      <span class="vintage__text">ESTATE | 2023 | GROWN</span>
      <span class="vintage__rule"></span>
    </div>
  </main>
</body>
</html>
```